Bag packaging design of sliced bread

The project is for design of line of sliced bread with different flavours. The brand of the bread will be "Velorasa". The shape of the bread will be oval. The bread will be packed in a bag. I attach the layout of the bag. The bag will be closed with a plastic clip. I attach images of similar products. The idea is to have one main design and then each colour to be different type of bread like those in the images 2 and 5.

```html
<!DOCTYPE html>
<html lang="ro">
<head>
<meta charset="utf-8">
<title>Velorasa – pâine feliată</title>
<link rel="stylesheet" href="https://fonts.googleapis.com/css2?family=Oswald:wght@400;500;700&display=swap">
<style>
  :root {
    --paper: #ffffff;
    --ink: #000000;
    --graham: #e97e22;
    --graham-soft: #f3b57a;
    --seeds: #802c28;
    --seeds-soft: #a9625d;
    --rye: #56d40a;
    --rye-soft: #a4ea78;
    --badge-green: #c3e04c;
    --vegan-teal: #22cfb4;
    --natural-ink: #2d3a1a;
    --pattern-tone: #ececec;
  }
  * { box-sizing: border-box; margin: 0; padding: 0; }
  html, body { width: 1200px; height: 630px; overflow: hidden; background: var(--paper); }
  body { position: relative; font-family: "Oswald", sans-serif; }

  .bag {
    position: absolute; top: 0; width: 242px; height: 547px;
    background: var(--paper); overflow: hidden;
  }
  .bag--graham { left: 99px; --tone: var(--graham); --tone-soft: var(--graham-soft); }
  .bag--seeds  { left: 533px; --tone: var(--seeds); --tone-soft: var(--seeds-soft); }
  .bag--rye    { left: 956px; --tone: var(--rye); --tone-soft: var(--rye-soft); }

  .bag__clip-band {
    position: absolute; left: 0; top: 0; width: 100%; height: 42px; background: var(--tone); z-index: 2;
  }
  .bag__hole {
    position: absolute; top: 7px; width: 28px; height: 28px; border-radius: 50%; background: var(--paper);
  }
  .bag__hole--left { left: 27px; }
  .bag__hole--right { left: 187px; }
  .bag--rye .bag__hole { border: 1px solid var(--ink); }

  .bag__pattern {
    position: absolute; left: 0; top: 42px; width: 100%; height: 260px;
    background: linear-gradient(180deg, var(--pattern-tone), #f7f7f7);
  }
  .bag__panel {
    position: absolute; left: 0; top: 0; width: 100%; height: 100%;
    background: var(--tone);
  }
  .bag--graham .bag__panel { clip-path: polygon(0 284px, 100% 193px, 100% 100%, 0 100%); }
  .bag--seeds .bag__panel,
  .bag--rye .bag__panel { clip-path: polygon(0 290px, 100% 225px, 100% 100%, 0 100%); }

  .bag__wheat {
    position: absolute; left: 0; bottom: 0; width: 165px; height: 100px;
    background: linear-gradient(30deg, var(--tone-soft), var(--tone) 85%);
    opacity: .8; z-index: 1;
  }

  .brand {
    position: absolute; left: 0; top: 170px; width: 242px; height: 190px; z-index: 3;
  }
  .brand svg { display: block; width: 100%; height: 100%; }
  .brand__name {
    font-family: "Oswald", sans-serif; font-weight: 500; font-size: 44px; fill: var(--paper);
  }

  .flavour {
    position: absolute; width: 92px; height: 92px; border-radius: 50%;
    background: var(--paper); color: var(--ink);
    display: flex; flex-direction: column; align-items: center; justify-content: center;
    text-align: center; line-height: 1.15; z-index: 5;
  }
  .bag--graham .flavour, .bag--rye .flavour { left: 71px; top: 357px; }
  .flavour--top { left: 76px; top: 70px; width: 94px; height: 94px; background: var(--seeds); color: var(--paper); }
  .flavour__kind { font-size: 14px; font-weight: 500; letter-spacing: 2px; }
  .flavour__sub { font-size: 8px; font-weight: 400; }
  .flavour__grain { font-size: 14px; font-weight: 500; letter-spacing: .5px; }
  .flavour__sliced {
    font-size: 8px; margin-top: 4px; display: flex; align-items: center; gap: 3px;
  }
  .flavour__sliced::before, .flavour__sliced::after {
    content: ""; width: 10px; height: 1px; background: currentColor;
  }
  .flavour--top .flavour__kind, .flavour--top .flavour__grain { font-size: 13px; }
  .flavour--top .flavour__sub { font-size: 7px; line-height: 1; }
  .flavour--top .flavour__sliced { margin-top: 2px; }
  .flavour--top .flavour__sliced::before, .flavour--top .flavour__sliced::after { display: none; }

  .badge {
    position: absolute; z-index: 4;
    display: flex; flex-direction: column; align-items: center; justify-content: center;
    text-align: center; line-height: 1;
  }
  .badge--vegan {
    left: 147px; top: 320px; width: 80px; height: 50px;
    background: var(--badge-green);
    border-radius: 60% 10% 60% 40%;
    transform: rotate(-14deg);
    color: var(--vegan-teal); font-size: 18px; font-weight: 500;
  }
  .badge--natural {
    left: 174px; top: 284px; width: 66px; height: 66px; border-radius: 50%;
    background: var(--badge-green); color: var(--natural-ink);
    outline: 1.5px dashed var(--badge-green); outline-offset: 3px;
  }
  .badge__big { font-size: 21px; font-weight: 400; }
  .badge__small { font-size: 11px; font-weight: 500; margin-top: 2px; }

  .weight {
    position: absolute; left: 170px; top: 506px; width: 64px; height: 30px;
    background: var(--paper); border-radius: 4px; z-index: 5;
    display: flex; align-items: center; justify-content: center;
    font-size: 23px; font-weight: 700; color: var(--ink); letter-spacing: .5px;
  }
</style>
</head>
<body>

  <section class="bag bag--graham" aria-label="Pâine cu făină Graham">
    <div class="bag__pattern" role="img" aria-label="Model repetat de spice de grâu negre pe alb"></div>
    <div class="bag__panel"></div>
    <div class="bag__clip-band"><span class="bag__hole bag__hole--left"></span><span class="bag__hole bag__hole--right"></span></div>
    <div class="bag__wheat" role="img" aria-label="Ilustrație cu spice de grâu desenate în alb"></div>
    <div class="brand">
      <svg viewBox="0 0 242 190">
        <ellipse cx="121" cy="97" rx="118" ry="84" transform="rotate(-20 121 97)" fill="#000"/>
        <text class="brand__name" x="121" y="112" text-anchor="middle" transform="rotate(-18 121 97)">Velorasa</text>
      </svg>
    </div>
    <div class="badge badge--vegan">Vegan</div>
    <div class="flavour">
      <span class="flavour__kind">PÂINE</span>
      <span class="flavour__sub">cu făină</span>
      <span class="flavour__grain">GRAHAM</span>
      <span class="flavour__sliced">feliată</span>
    </div>
    <div class="weight">500g</div>
  </section>

  <section class="bag bag--seeds" aria-label="Pâine cu semințe și cereale">
    <div class="bag__pattern" role="img" aria-label="Model repetat de spice de grâu negre pe alb"></div>
    <div class="bag__panel"></div>
    <div class="bag__clip-band"><span class="bag__hole bag__hole--left"></span><span class="bag__hole bag__hole--right"></span></div>
    <div class="bag__wheat" role="img" aria-label="Ilustrație cu spice de grâu desenate în alb"></div>
    <div class="flavour flavour--top">
      <span class="flavour__kind">PÂINE</span>
      <span class="flavour__sub">cu</span>
      <span class="flavour__grain">SEMINȚE</span>
      <span class="flavour__sub">și</span>
      <span class="flavour__grain">SEREALE</span>
      <span class="flavour__sliced">feliată</span>
    </div>
    <div class="brand">
      <svg viewBox="0 0 242 190">
        <ellipse cx="121" cy="97" rx="118" ry="84" transform="rotate(-20 121 97)" fill="#000"/>
        <text class="brand__name" x="121" y="112" text-anchor="middle" transform="rotate(-18 121 97)">Velorasa</text>
      </svg>
    </div>
    <div class="badge badge--natural">
      <span class="badge__big">100%</span>
      <span class="badge__small">natural</span>
    </div>
    <div class="weight">500g</div>
  </section>

  <section class="bag bag--rye" aria-label="Pâine cu făină de secară">
    <div class="bag__pattern" role="img" aria-label="Model repetat de spice de grâu conturate pe alb"></div>
    <div class="bag__panel"></div>
    <div class="bag__clip-band"><span class="bag__hole bag__hole--left"></span><span class="bag__hole bag__hole--right"></span></div>
    <div class="bag__wheat" role="img" aria-label="Ilustrație cu spice de grâu desenate în alb"></div>
    <div class="brand">
      <svg viewBox="0 0 242 190">
        <ellipse cx="121" cy="97" rx="118" ry="84" transform="rotate(-20 121 97)" fill="#000"/>
        <text class="brand__name" x="121" y="112" text-anchor="middle" transform="rotate(-18 121 97)">Velorasa</text>
      </svg>
    </div>
    <div class="flavour">
      <span class="flavour__kind">PÂINE</span>
      <span class="flavour__sub">cu făină de</span>
      <span class="flavour__grain">SECARĂ</span>
      <span class="flavour__sliced">feliată</span>
    </div>
    <div class="weight">500g</div>
  </section>

</body>
</html>
```